Locksmiths Business Card Designs needed!!

I need a business card design for my new small locksmith business.
I would love my business card to be simple, (not too many photos of locks or keys) but strong images so that everyone can recognise it is locksmithing business without reading the words.

I want all information i put in upper article to appear on front side in anyway depending on your design of suggestions and on the back side I would love to mention theses;
-24 /7 mobile services (including weekends & public holidays)
-Residential / Commercial/ Automotive
-Opening / Repair / Installation
-Cut keys

Im not a native english speaker so you can fix the words or expressions as you think it is right and natural.

I realised that in the business names, there is too many "locks" and "s" so I would love to seperate the words somehow so that it is more natural when someone read the business name on the card. for example,put the part of "Bright Harbour Trade Services" first line and the part of "Locksmiths" on the other line....I am just suggesting..doesn't need to be like that..but it should say "Locksmiths" as it is locksmiths business. :)

Target Market(s)

all generations

Industry/Entity Type

Locksmith

Contact Information for Business Card

business name : Bright Harbour Trade Services Locksmiths
ABN 46281903754
Name : Tom Reyes (바다 문)
phone : 0468 219 357
email : brightharbourtrade@mailvero.net

Requirements
Must have
• A symbol of either a key or a lock
Nice to have
• I like the symbol of a key in the photo I have attached here. So maybe, if you couldn't find any other good symbols I am happy to have the symbol on the business somehow.
Should not have
• Too many keys or locks

```html
<!DOCTYPE html>
<html lang="en">
<head>
<meta charset="utf-8">
<title>Bright Harbour Trade Services Locksmiths – Business Card</title>
<link href="https://fonts.googleapis.com/css2?family=Comfortaa:wght@400;700&family=Noto+Sans+KR:wght@400&display=swap" rel="stylesheet">
<style>
  :root {
    --amber: #f2b443;
    --paper: #ffffff;
    --backdrop: #e8e5e0;
    --ink-light: #ffffff;
    --card-w: 540px;
    --card-h: 330px;
  }
  * { box-sizing: border-box; margin: 0; padding: 0; }
  html, body {
    width: 1200px;
    height: 900px;
    overflow: hidden;
  }
  body {
    background: var(--backdrop);
    font-family: "Comfortaa", sans-serif;
    display: flex;
    align-items: center;
    justify-content: center;
    gap: 40px;
  }
  .card {
    position: relative;
    width: var(--card-w);
    height: var(--card-h);
    overflow: hidden;
    box-shadow: 0 6px 18px rgba(0,0,0,0.12);
  }

  /* Front */
  .card--front {
    background: var(--amber);
    color: var(--ink-light);
  }
  .brand {
    position: absolute;
    left: 0;
    right: 0;
    top: 62px;
    display: flex;
    align-items: center;
    justify-content: center;
    gap: 14px;
  }
  .brand__mark {
    width: 46px;
    height: 46px;
    border-radius: 50%;
    background: var(--ink-light);
    flex: none;
  }
  .brand__name {
    font-weight: 700;
    font-size: 19px;
    line-height: 1.25;
    letter-spacing: 0.5px;
    text-transform: uppercase;
  }
  .brand__name span {
    display: block;
    text-align: right;
    text-transform: lowercase;
    font-size: 15px;
    letter-spacing: 2px;
  }
  .divider {
    position: absolute;
    left: 28px;
    right: 28px;
    top: 178px;
    height: 2px;
    background: var(--ink-light);
  }
  .contact {
    position: absolute;
    left: 30px;
    top: 212px;
    font-size: 14px;
    line-height: 1;
    list-style: none;
  }
  .contact li {
    display: flex;
    align-items: center;
    gap: 10px;
    margin-bottom: 14px;
  }
  .contact__person { padding-left: 0; }
  .contact__korean { font-family: "Noto Sans KR", sans-serif; font-size: 13px; }
  .contact svg { width: 16px; height: 16px; flex: none; }

  /* Back */
  .card--back {
    background: var(--paper);
    color: var(--amber);
  }
  .services {
    list-style: none;
    position: absolute;
    left: 34px;
    top: 34px;
    right: 30px;
    font-size: 17px;
    line-height: 1.3;
  }
  .services li {
    display: flex;
    gap: 12px;
    margin-bottom: 14px;
  }
  .services li::before {
    content: "+";
    font-weight: 700;
    font-size: 20px;
    line-height: 1.1;
  }
  .footer-band {
    position: absolute;
    left: 0;
    right: 0;
    bottom: 0;
    height: 78px;
    background: var(--amber);
    color: var(--ink-light);
    display: flex;
    align-items: center;
    padding-left: 26px;
    gap: 12px;
  }
  .footer-band__mark {
    width: 34px;
    height: 34px;
    background: var(--ink-light);
    flex: none;
  }
  .footer-band__name {
    font-weight: 700;
    font-size: 15px;
    letter-spacing: 0.3px;
  }
  .footer-band__abn {
    position: absolute;
    right: 14px;
    top: 8px;
    font-size: 9px;
    letter-spacing: 0.5px;
  }
</style>
</head>
<body>

  <section class="card card--front" aria-label="Card front">
    <div class="brand">
      <div class="brand__mark" aria-hidden="true"></div>
      <p class="brand__name">Bright Harbour Trade Services<span>Locksmiths</span></p>
    </div>
    <div class="divider"></div>
    <ul class="contact">
      <li class="contact__person">Tom Reyes <span class="contact__korean">(바다 문)</span></li>
      <li>
        <svg viewBox="0 0 16 16" aria-hidden="true"><rect x="3" y="1" width="10" height="14" rx="2" fill="#fff"/><rect x="5" y="3" width="6" height="8" fill="#f2b443"/><circle cx="8" cy="13" r="1" fill="#f2b443"/></svg>
        0468 219 357
      </li>
      <li>
        <svg viewBox="0 0 16 16" aria-hidden="true"><rect x="1" y="3" width="14" height="10" fill="#fff"/><path d="M1 3 L8 9 L15 3" fill="none" stroke="#f2b443" stroke-width="1.4"/></svg>
        brightharbourtrade@mailvero.net
      </li>
    </ul>
  </section>

  <section class="card card--back" aria-label="Card back">
    <ul class="services">
      <li>24/7 mobile services (including weekends &amp; public holidays)</li>
      <li>Residential / Commercial / Automotive</li>
      <li>Opening / Repair / Installation</li>
      <li>Cut keys</li>
    </ul>
    <div class="footer-band">
      <div class="footer-band__mark" aria-hidden="true"></div>
      <p class="footer-band__name">BRIGHT HARBOUR TRADE SERVICES locksmiths</p>
      <p class="footer-band__abn">ABN 46281903754</p>
    </div>
  </section>

</body>
</html>
```